Powerpoint for Talveo

Check out the attached sample powerpoint, we would like our powerpoint to look similar to this. in the slides where you see monitor, we would like to put pics of different industries in each monitor. like images of hotels, hospitals, large business with multiple locations, small business, retail)

The Powerpoint will contain the below slides

About US
Our Guarantee – 100% satisfaction and 30% cost savings
Products & Services ( Hosted PBX phone system, SIP Trunking, Network security solutions, commercial grade band width and firewalls, IT Network design services)
Features ( One slide for this we will enter the content)
Industries ( Small business, hospitality, hospitals, Banks for secure voice, Large business with multiple locations, Retail)
Hosted PBX
Why Talveo
Channel partners
Our customers
Contact us
Updates

Target Market(s)

Small business, hospitality, hospitals, Banks for secure voice, Large business with multiple locations, Retail, law firms, insurance companies

Industry/Entity Type

Security

Requirements
Must have
• Please look at the attached powerpoint for color, style, font details

```html
<!DOCTYPE html>
<html lang="en">
<head>
<meta charset="utf-8">
<title>Talveo Presentation</title>
<link href="https://fonts.googleapis.com/css2?family=Open+Sans:wght@300;400;600&display=swap" rel="stylesheet">
<style>
:root{
  --page:#d9d9d9;
  --paper:#ffffff;
  --body-top:#f4f4f4;
  --body-bottom:#e4e4e4;
  --ink:#3a3a3a;
  --ink-soft:#444;
  --accent:#1aa6e0;
  --frame:#2a2a2a;
  --silver-top:#e9e9eb;
  --silver-bottom:#b9b9bd;
}
*{margin:0;padding:0;box-sizing:border-box}
html,body{width:1200px;height:900px;overflow:hidden}
body{background:var(--page);font-family:"Open Sans",Arial,sans-serif;color:var(--ink);position:relative}
.slide{position:absolute;width:583px;height:437px;background:var(--paper);overflow:hidden;box-shadow:0 1px 3px rgba(0,0,0,.35)}
.slide--industry-banks{left:10px;top:12px}
.slide--industry-business{left:605px;top:12px}
.slide--awards{left:10px;top:457px}
.slide--contact{left:605px;top:457px}
.slide__body{position:absolute;left:0;right:0;top:30px;bottom:44px;background:linear-gradient(var(--body-top),var(--body-bottom))}
.slide--awards .slide__body,.slide--contact .slide__body{bottom:46px}
.page-number{position:absolute;left:23px;bottom:16px;font-size:7px;color:var(--ink)}
.industry-title{position:absolute;left:40px;top:74px;font-size:25px;line-height:35px;font-weight:400;color:var(--ink)}
.monitor{position:absolute;left:193px;top:36px;width:400px;height:345px}
.monitor__frame{position:absolute;left:0;top:0;right:0;height:240px;background:var(--frame);border-radius:9px 0 0 0}
.monitor__screen{position:absolute;left:17px;top:19px;right:0;height:221px}
.monitor__screen--laptop{background:linear-gradient(135deg,#4a4f5e 0%,#8d93a6 40%,#c9cbd6 70%,#e8e6ea 100%)}
.monitor__screen--team{background:linear-gradient(120deg,#c9d6e6 0%,#2b3a5c 35%,#e6eaf0 55%,#1f2c4a 80%,#cfd8e4 100%)}
.monitor__chin{position:absolute;left:0;right:0;top:240px;height:57px;background:linear-gradient(var(--silver-top),var(--silver-bottom));border-radius:0 0 0 9px}
.monitor__stand{position:absolute;left:150px;top:297px}
.awards-title{position:absolute;left:40px;top:38px;font-size:28px;font-weight:300;color:var(--ink);letter-spacing:.3px}
.awards-intro{position:absolute;left:40px;top:84px;width:470px;font-size:9.6px;line-height:20.5px;color:var(--ink-soft)}
.award{position:absolute;top:174px;width:160px}
.award--rating{left:88px}
.award--leader{left:358px}
.award__title{font-size:10.5px;font-weight:400;color:var(--accent);margin-bottom:7px}
.award__text{font-size:9.2px;line-height:13.5px;color:var(--ink-soft)}
.footer-brand{position:absolute;right:20px;bottom:12px;display:flex;align-items:center;gap:4px;font-size:11px;color:var(--ink)}
.footer-brand__mark{width:9px;height:9px;background:var(--accent)}
.brand{position:absolute;left:62px;top:136px;display:flex;align-items:center;gap:10px}
.brand__mark{width:46px;height:46px;background:var(--accent)}
.brand__name{font-size:32px;font-weight:600;color:var(--ink);letter-spacing:.5px}
.tagline{position:absolute;left:278px;top:157px;font-size:11px;color:var(--ink)}
.contact{position:absolute;left:278px;top:221px;font-size:11px;line-height:16px;color:var(--ink)}
.contact__label{margin-bottom:10px}
.contact__block{margin-bottom:10px}
.contact__web{color:var(--accent);letter-spacing:2.5px}
</style>
</head>
<body>

<section class="slide slide--industry-banks">
  <div class="slide__body"></div>
  <h2 class="industry-title">Banks for<br>secure voice</h2>
  <div class="monitor">
    <div class="monitor__frame"></div>
    <div class="monitor__screen monitor__screen--laptop" role="img" aria-label="Photo of hands typing on a laptop keyboard"></div>
    <div class="monitor__chin"></div>
    <svg class="monitor__stand" width="130" height="48" viewBox="0 0 130 48">
      <defs><linearGradient id="standA" x1="0" y1="0" x2="0" y2="1"><stop offset="0" stop-color="#a9a9ad"/><stop offset="1" stop-color="#e6e6e8"/></linearGradient></defs>
      <path d="M22 0 H108 L118 40 Q120 46 112 46 H18 Q10 46 12 40 Z" fill="url(#standA)"/>
    </svg>
  </div>
  <p class="page-number">Page 9</p>
</section>

<section class="slide slide--industry-business">
  <div class="slide__body"></div>
  <h2 class="industry-title">Large<br>business<br>with<br>multiple<br>locations</h2>
  <div class="monitor">
    <div class="monitor__frame"></div>
    <div class="monitor__screen monitor__screen--team" role="img" aria-label="Photo of business people in suits reviewing documents at a desk"></div>
    <div class="monitor__chin"></div>
    <svg class="monitor__stand" width="130" height="48" viewBox="0 0 130 48">
      <defs><linearGradient id="standB" x1="0" y1="0" x2="0" y2="1"><stop offset="0" stop-color="#a9a9ad"/><stop offset="1" stop-color="#e6e6e8"/></linearGradient></defs>
      <path d="M22 0 H108 L118 40 Q120 46 112 46 H18 Q10 46 12 40 Z" fill="url(#standB)"/>
    </svg>
  </div>
  <p class="page-number">Page 10</p>
</section>

<section class="slide slide--awards">
  <div class="slide__body"></div>
  <h2 class="awards-title">AWARDS + HONORS</h2>
  <p class="awards-intro">The biggest Award for our team is our customers’ success. It’s always a pleasure to get positive feedbacks and appreciation from clients whose success we helped achieve. Each member of Talveo rejoices every time one of our customers gets back to us with a new reference for our services</p>
  <div class="award award--rating">
    <h3 class="award__title">Business Rating</h3>
    <p class="award__text">Our customers love our services and the savings we provide to them</p>
  </div>
  <div class="award award--leader">
    <h3 class="award__title">Leader of Industry</h3>
    <p class="award__text">Kestrel Soft Corp. was named the Company of the Year 2010 in Ukraine in the Standard Software Development category.</p>
  </div>
  <p class="page-number">Page 13</p>
  <div class="footer-brand"><span class="footer-brand__mark"></span><span>Talveo</span></div>
</section>

<section class="slide slide--contact">
  <div class="slide__body"></div>
  <div class="brand"><span class="brand__mark"></span><span class="brand__name">Talveo</span></div>
  <p class="tagline">Cloud. Mobile. Ecommerce. Design.</p>
  <div class="contact">
    <p class="contact__label">CONTACT</p>
    <p class="contact__block">4120 Meridian Pkwy, suite 210<br>Dallas TX 75240</p>
    <p>T&nbsp; 972.555.0148<br>F&nbsp; 469-555-0193</p>
    <p class="contact__web">talveo.com</p>
  </div>
</section>

</body>
</html>
```